Industrial Rubber Manufacturer Trade-Show Flyer

We are looking for a flyer to hand out to potential customers while walking the floors of a trade show. I have attached a document coming several of the product lines we currently do. Please refer to our website www.corvanpolymers.com for the color we are looking for the gold, brownish, and black colors in our header. I don't have any pictures besides our one of the building. We would like to have rubber extrusion related pictures and / or displays of industries we sell to
Target Market(s)
automotive, rv industry
Industry/Entity Type
Industrial
Font styles to use
Requirements
Must have
- clean look and feel. display information about the company.

```html
<!DOCTYPE html>
<html lang="en">
<head>
<meta charset="utf-8">
<title>Corvan Polymers – Trade Show Flyer</title>
<link href="https://fonts.googleapis.com/css2?family=Fira+Sans:wght@400;500;600;700&family=Open+Sans:wght@400;600&display=swap" rel="stylesheet">
<style>
  :root{
    --page:#141414;
    --card-dark:#262626;
    --band-dark:#1c1c1c;
    --gold:#c2a36b;
    --gold-light:#e2c98f;
    --gold-text:#d7b77a;
    --gold-head:#b8975a;
    --ink:#1b1b1b;
    --white:#ffffff;
    --body-light:#f0f0f0;
  }
  *{margin:0;padding:0;box-sizing:border-box}
  html,body{width:960px;height:1200px;overflow:hidden;background:var(--page)}
  body{position:relative;font-family:"Open Sans",Arial,sans-serif}

  .card{position:absolute;left:80px;width:800px;overflow:hidden;box-shadow:0 4px 12px rgba(0,0,0,.6)}
  .card--front{top:69px;height:515px;background:var(--card-dark)}
  .card--back{top:614px;height:516px;background:var(--white)}
  .card svg.shapes{position:absolute;inset:0}

  .brand{position:absolute;display:flex;align-items:center;gap:10px}
  .brand__dot{border-radius:50%;flex:none}
  .brand__name{font-family:"Open Sans",Arial,sans-serif;font-weight:600;text-transform:uppercase;line-height:1.15}

  .front__brand{left:520px;top:45px}
  .front__brand .brand__dot{width:48px;height:48px;border:5px solid var(--gold)}
  .front__brand .brand__name{color:var(--white);font-size:14px;letter-spacing:4.4px}

  .front__intro{position:absolute;left:508px;top:145px;width:268px;color:var(--body-light);
    font-size:12px;line-height:15.4px;text-align:center}

  .materials{position:absolute;left:589px;top:248px}
  .materials__title{font-family:"Fira Sans",Arial,sans-serif;font-weight:600;color:var(--white);font-size:21px;letter-spacing:.3px}
  .materials__list{list-style:none;margin-top:6px}
  .materials__item{display:flex;align-items:center;gap:4px;height:21.8px;color:var(--gold-text);
    font-family:"Fira Sans",Arial,sans-serif;font-weight:500;font-size:13px}
  .materials__item svg{width:11px;height:11px;flex:none}

  .capabilities{position:absolute;left:35px;top:38px}
  .capabilities__title{font-family:"Fira Sans",Arial,sans-serif;font-weight:600;color:var(--gold-head);font-size:22px;letter-spacing:.2px}
  .capabilities__sub{font-family:"Fira Sans",Arial,sans-serif;color:var(--gold-head);font-size:13px;margin-top:1px}
  .capabilities__list{font-family:"Fira Sans",Arial,sans-serif;font-weight:500;color:var(--ink);font-size:13.5px;line-height:21.5px;margin-top:5px}

  .industries__title{position:absolute;left:35px;top:178px;font-family:"Fira Sans",Arial,sans-serif;font-weight:600;
    color:var(--ink);font-size:22px;letter-spacing:.3px}
  .industries__rule{position:absolute;left:253px;top:191px;width:350px;height:1px;
    background:linear-gradient(90deg,var(--gold),rgba(194,163,107,0))}
  .industries__rule::before{content:"";position:absolute;left:-3px;top:-2px;width:5px;height:5px;border-radius:50%;background:var(--gold)}

  .industry{position:absolute;width:130px;margin-left:-65px;text-align:center}
  .industry__photo{width:104px;height:104px;margin:0 auto;border-radius:50%;border:3px solid var(--white);
    box-shadow:0 1px 3px rgba(0,0,0,.25)}
  .industry__label{margin-top:10px;font-family:"Fira Sans",Arial,sans-serif;font-size:12.5px;color:var(--ink);white-space:nowrap}

  .back__brand{left:640px;top:38px}
  .back__brand .brand__dot{width:30px;height:30px;border:3px solid var(--ink)}
  .back__brand .brand__name{color:var(--ink);font-size:9px;letter-spacing:2.6px}
  .back__address{position:absolute;left:643px;top:73px;font-family:"Fira Sans",Arial,sans-serif;font-size:12px;line-height:15.6px;color:var(--ink);font-style:normal}
  .back__contact{position:absolute;left:590px;top:464px;font-family:"Fira Sans",Arial,sans-serif;font-size:12px;line-height:15.6px;color:var(--white)}
</style>
</head>
<body>

<section class="card card--front">
  <svg class="shapes" viewBox="0 0 800 515" preserveAspectRatio="none">
    <defs>
      <linearGradient id="factoryTone" x1="0" y1="0" x2="1" y2="1">
        <stop offset="0" stop-color="#8a8580"/>
        <stop offset=".45" stop-color="#6b6864"/>
        <stop offset="1" stop-color="#9c9894"/>
      </linearGradient>
      <linearGradient id="goldSwoosh" x1="0" y1="0" x2="1" y2="1">
        <stop offset="0" stop-color="#b4955b"/>
        <stop offset="1" stop-color="#d8c08e"/>
      </linearGradient>
    </defs>
    <path d="M0,0 L300,0 Q640,120 600,515 L0,515 Z" fill="var(--band-dark)"/>
    <path d="M0,0 L218,0 Q580,130 552,515 L0,515 Z" fill="url(#factoryTone)" role="img" aria-label="Photo of a technician operating a rubber extrusion line in the factory"/>
    <path d="M218,0 Q580,130 552,515" fill="none" stroke="var(--gold)" stroke-width="6"/>
    <path d="M0,330 Q80,450 360,515 L0,515 Z" fill="url(#goldSwoosh)" opacity=".92"/>
    <path d="M0,315 Q60,440 330,515" fill="none" stroke="var(--gold-light)" stroke-width="2" opacity=".7"/>
  </svg>

  <div class="brand front__brand">
    <span class="brand__dot"></span>
    <span class="brand__name">Corvan<br>Polymers</span>
  </div>

  <p class="front__intro">Corvan Polymers extrudes organic and silicone rubber in dense and sponge compounds to the demanding quality standards of ASTM, SAE, JIS, Mil Specs and other organizations. We deliver competitively priced custom extrusions through efficient process control in compliance with ISO 9001-2008 standards.</p>

  <div class="materials">
    <h2 class="materials__title">MATERIALS</h2>
    <ul class="materials__list">
      <li class="materials__item" style="margin-left:8px"><svg viewBox="0 0 12 12"><circle cx="6" cy="6" r="5" fill="none" stroke="currentColor" stroke-width="1.2"/><path d="M3.5 6.2 5.3 8 8.8 3.8" fill="none" stroke="currentColor" stroke-width="1.3"/></svg>EPDM (Dense / Sponge)</li>
      <li class="materials__item" style="margin-left:19px"><svg viewBox="0 0 12 12"><circle cx="6" cy="6" r="5" fill="none" stroke="currentColor" stroke-width="1.2"/><path d="M3.5 6.2 5.3 8 8.8 3.8" fill="none" stroke="currentColor" stroke-width="1.3"/></svg>Silicone</li>
      <li class="materials__item" style="margin-left:26px"><svg viewBox="0 0 12 12"><circle cx="6" cy="6" r="5" fill="none" stroke="currentColor" stroke-width="1.2"/><path d="M3.5 6.2 5.3 8 8.8 3.8" fill="none" stroke="currentColor" stroke-width="1.3"/></svg>Nitrile</li>
      <li class="materials__item" style="margin-left:34px"><svg viewBox="0 0 12 12"><circle cx="6" cy="6" r="5" fill="none" stroke="currentColor" stroke-width="1.2"/><path d="M3.5 6.2 5.3 8 8.8 3.8" fill="none" stroke="currentColor" stroke-width="1.3"/></svg>Neoprene</li>
      <li class="materials__item" style="margin-left:42px"><svg viewBox="0 0 12 12"><circle cx="6" cy="6" r="5" fill="none" stroke="currentColor" stroke-width="1.2"/><path d="M3.5 6.2 5.3 8 8.8 3.8" fill="none" stroke="currentColor" stroke-width="1.3"/></svg>SBR</li>
      <li class="materials__item" style="margin-left:47px"><svg viewBox="0 0 12 12"><circle cx="6" cy="6" r="5" fill="none" stroke="currentColor" stroke-width="1.2"/><path d="M3.5 6.2 5.3 8 8.8 3.8" fill="none" stroke="currentColor" stroke-width="1.3"/></svg>Polyisoprene</li>
      <li class="materials__item" style="margin-left:50px"><svg viewBox="0 0 12 12"><circle cx="6" cy="6" r="5" fill="none" stroke="currentColor" stroke-width="1.2"/><path d="M3.5 6.2 5.3 8 8.8 3.8" fill="none" stroke="currentColor" stroke-width="1.3"/></svg>Dual Duro</li>
      <li class="materials__item" style="margin-left:53px"><svg viewBox="0 0 12 12"><circle cx="6" cy="6" r="5" fill="none" stroke="currentColor" stroke-width="1.2"/><path d="M3.5 6.2 5.3 8 8.8 3.8" fill="none" stroke="currentColor" stroke-width="1.3"/></svg>TPV / TPE / TPV</li>
      <li class="materials__item" style="margin-left:56px"><svg viewBox="0 0 12 12"><circle cx="6" cy="6" r="5" fill="none" stroke="currentColor" stroke-width="1.2"/><path d="M3.5 6.2 5.3 8 8.8 3.8" fill="none" stroke="currentColor" stroke-width="1.3"/></svg>PVC (Flexible)</li>
    </ul>
  </div>
</section>

<section class="card card--back">
  <svg class="shapes" viewBox="0 0 800 516" preserveAspectRatio="none">
    <defs>
      <linearGradient id="buildingTone" x1="0" y1="0" x2="0" y2="1">
        <stop offset="0" stop-color="#a9c6e6"/>
        <stop offset=".5" stop-color="#d6e2ea"/>
        <stop offset=".6" stop-color="#8f9488"/>
        <stop offset="1" stop-color="#4f5a38"/>
      </linearGradient>
      <linearGradient id="creamToGold" x1="0" y1="0" x2="0" y2="1">
        <stop offset="0" stop-color="#ffffff"/>
        <stop offset=".38" stop-color="#ffffff"/>
        <stop offset="1" stop-color="#c9ab72"/>
      </linearGradient>
    </defs>
    <rect x="0" y="0" width="800" height="516" fill="url(#buildingTone)" role="img" aria-label="Aerial photo of the company plant, lawn and parking lot"/>
    <path d="M0,0 L546,0 Q610,260 410,516 L0,516 Z" fill="var(--gold)" opacity=".85"/>
    <path d="M0,0 L530,0 Q592,260 390,516 L0,516 Z" fill="url(#creamToGold)"/>
  </svg>

  <div class="capabilities">
    <h2 class="capabilities__title">CORE CAPABILITIES</h2>
    <p class="capabilities__sub">Industry leader in sponge and taping applications</p>
    <p class="capabilities__list">Tooling &amp; Die Shop Cutting • Taping &nbsp;• Hole Punching<br>Notching • Vulcanized Splicing • Flocking</p>
  </div>

  <h2 class="industries__title">INDUSTRIES SERVER</h2>
  <div class="industries__rule"></div>

  <div class="industry" style="left:86px;top:220px">
    <div class="industry__photo" role="img" aria-label="Recreational vehicle photo" style="background:linear-gradient(160deg,#4d5a4a,#b8bcbf 55%,#6b6e70)"></div>
    <p class="industry__label">Recreational Vehicles</p>
  </div>
  <div class="industry" style="left:200px;top:220px">
    <div class="industry__photo" role="img" aria-label="Industrial plant photo" style="background:linear-gradient(180deg,#5f8fc8,#a9c7e6 50%,#4a4d52)"></div>
    <p class="industry__label">Industrial</p>
  </div>
  <div class="industry" style="left:314px;top:220px">
    <div class="industry__photo" role="img" aria-label="Automotive motion photo" style="background:radial-gradient(circle at 50% 45%,#e8f1fb,#6f93c2 55%,#2d3e5c)"></div>
    <p class="industry__label">Automotive</p>
  </div>
  <div class="industry" style="left:429px;top:220px">
    <div class="industry__photo" role="img" aria-label="Window and door interior photo" style="background:linear-gradient(180deg,#d9dcd6,#7b8a6a 55%,#b9b2a6)"></div>
    <p class="industry__label">Window &amp; Door</p>
  </div>
  <div class="industry" style="left:86px;top:364px">
    <div class="industry__photo" role="img" aria-label="Wheat field photo" style="background:linear-gradient(180deg,#7fb43a,#3f7e25 60%,#9ccc4c)"></div>
    <p class="industry__label">Agriculture</p>
  </div>
  <div class="industry" style="left:202px;top:364px">
    <div class="industry__photo" role="img" aria-label="Mining dump truck photo" style="background:linear-gradient(180deg,#9aa0a4,#c8a43c 50%,#6b6a66)"></div>
    <p class="industry__label">Heavy Equipment</p>
  </div>
  <div class="industry" style="left:318px;top:364px">
    <div class="industry__photo" role="img" aria-label="Light bulb in hand photo" style="background:radial-gradient(circle at 50% 35%,#f7e3a0,#b0935a 55%,#2a2620)"></div>
    <p class="industry__label">Electrical &amp; Lighting</p>
  </div>

  <div class="brand back__brand">
    <span class="brand__dot"></span>
    <span class="brand__name">Corvan<br>Polymers</span>
  </div>
  <address class="back__address">Corvan Polymers<br>4810 County Road 12<br>Marlow, OH 44390</address>
  <p class="back__contact">www.corvanpolymers.com<br>info@corvanpolymers.com</p>
</section>

</body>
</html>
```